Horse related business entrepreneur needs a business card

I need a business card design for my horse related business. The enterprise is Copper Vale LLC and I have 3 businesses (headquartered at 2 locations): 1. property management where we rent horse stalls and apartments at a thoroughbred training center outside Ocala; 2. a medium sized transportation service in central Florida that sells horse bedding and removes used horse bedding from horse farms; and horse racing

```html
<!DOCTYPE html>
<html lang="en">
<head>
<meta charset="utf-8">
<title>Copper Vale LLC – Business Card</title>
<link href="https://fonts.googleapis.com/css2?family=Cinzel:wght@400;500&family=Lato:wght@400&display=swap" rel="stylesheet">
<style>
  :root {
    --backdrop: #2a2a2a;
    --card-blue: #42617d;
    --card-white: #ffffff;
    --logo-gray: #8c8c8c;
    --ink-light: #ffffff;
  }
  html, body {
    margin: 0;
    padding: 0;
    width: 1200px;
    height: 1200px;
    overflow: hidden;
    background: var(--backdrop);
  }
  .canvas {
    position: relative;
    width: 1200px;
    height: 1200px;
  }
  .card {
    position: absolute;
    top: 310px;
    width: 364px;
    height: 593px;
    box-sizing: border-box;
  }
  .card-front {
    left: 234px;
    background: var(--card-blue);
    color: var(--ink-light);
    text-align: center;
  }
  .card-back {
    left: 628px;
    width: 368px;
    background: var(--card-white);
    border-top: 66px solid var(--card-blue);
    border-bottom: 50px solid var(--card-blue);
  }
  .company-name {
    position: absolute;
    top: 82px;
    left: 0;
    right: 0;
    margin: 0;
    font-family: "Cinzel", serif;
    font-weight: 500;
    font-size: 52px;
    letter-spacing: 0.5px;
    line-height: 1;
  }
  .company-suffix {
    position: absolute;
    top: 144px;
    left: 52px;
    right: 52px;
    display: flex;
    align-items: center;
    gap: 12px;
    font-family: "Cinzel", serif;
    font-weight: 500;
    font-size: 22px;
    line-height: 1;
  }
  .rule {
    flex: 1;
    height: 2px;
    background: currentColor;
  }
  .person-name {
    position: absolute;
    top: 222px;
    left: 0;
    right: 0;
    margin: 0;
    font-family: "Cinzel", serif;
    font-weight: 500;
    font-size: 26px;
    line-height: 1;
  }
  .person-role {
    position: absolute;
    top: 249px;
    left: 0;
    right: 0;
    margin: 0;
    font-family: "Lato", sans-serif;
    font-size: 16px;
  }
  .divider {
    position: absolute;
    left: 88px;
    right: 86px;
    display: flex;
    align-items: center;
    gap: 4px;
  }
  .divider .rule { height: 1px; }
  .divider-contact { top: 287px; }
  .divider-address { top: 405px; }
  .icon-box {
    width: 20px;
    height: 17px;
    background: var(--ink-light);
    display: flex;
    align-items: center;
    justify-content: center;
  }
  .icon-box svg { display: block; }
  .details {
    position: absolute;
    left: 0;
    right: 0;
    margin: 0;
    font-family: "Lato", sans-serif;
    font-size: 17px;
    line-height: 21.5px;
    font-style: normal;
  }
  .contact-lines { top: 316px; }
  .address-primary { top: 437px; }
  .address-secondary { top: 488px; }
  .brand-mark {
    position: absolute;
    left: 96px;
    top: 110px;
    width: 172px;
    height: 172px;
    box-sizing: border-box;
    border: 5px solid var(--card-blue);
  }
  .brand-name {
    position: absolute;
    top: 296px;
    left: 0;
    right: 0;
    margin: 0;
    text-align: center;
    font-family: "Cinzel", serif;
    font-weight: 500;
    font-size: 36px;
    line-height: 1;
    color: var(--card-blue);
  }
  .brand-suffix {
    position: absolute;
    top: 338px;
    left: 92px;
    right: 92px;
    display: flex;
    align-items: center;
    gap: 10px;
    font-family: "Cinzel", serif;
    font-weight: 500;
    font-size: 16px;
    line-height: 1;
    color: var(--card-blue);
  }
</style>
</head>
<body>
<main class="canvas">
  <section class="card card-front" aria-label="Business card front">
    <h1 class="company-name">Copper Vale</h1>
    <div class="company-suffix"><span class="rule"></span><span>LLC</span><span class="rule"></span></div>

    <h2 class="person-name">Owen Thorley</h2>
    <p class="person-role">Owner</p>

    <div class="divider divider-contact">
      <span class="rule"></span>
      <span class="icon-box" aria-label="Phone">
        <svg width="14" height="11" viewBox="0 0 14 11"><path d="M1 3 Q7 -1 13 3 L11.5 5 L9.5 4 L9.5 3 Q7 2 4.5 3 L4.5 4 L2.5 5 Z M3 6 H11 V10 H3 Z" fill="var(--card-blue)"/></svg>
      </span>
      <span class="icon-box" aria-label="Fax">
        <svg width="14" height="12" viewBox="0 0 14 12"><rect x="4" y="0.5" width="6" height="3" fill="var(--card-blue)"/><rect x="1" y="4" width="12" height="5" fill="var(--card-blue)"/><rect x="4" y="7" width="6" height="4.5" fill="var(--card-blue)" stroke="#fff" stroke-width="0.8"/></svg>
      </span>
      <span class="icon-box" aria-label="Email">
        <svg width="14" height="10" viewBox="0 0 14 10"><rect x="0.5" y="0.5" width="13" height="9" fill="var(--card-blue)"/><path d="M1 1 L7 6 L13 1" fill="none" stroke="#fff" stroke-width="1"/></svg>
      </span>
      <span class="rule"></span>
    </div>

    <address class="details contact-lines">
      (352) 555-0147<br>
      (352) 555-0183<br>
      owen@coppervale.com
    </address>

    <div class="divider divider-address" style="left:88px;right:86px;">
      <span class="rule"></span>
      <span class="icon-box" aria-label="Location" style="width:20px;height:19px;">
        <svg width="10" height="14" viewBox="0 0 10 14"><path d="M5 0 A5 5 0 0 1 10 5 C10 8 5 14 5 14 C5 14 0 8 0 5 A5 5 0 0 1 5 0 Z" fill="var(--card-blue)"/><circle cx="5" cy="5" r="1.8" fill="#fff"/></svg>
      </span>
      <span class="rule"></span>
    </div>

    <address class="details address-primary">
      1720 SE 96th Lane<br>
      Fairfield, FL 32634
    </address>
    <address class="details address-secondary">
      815 Millstone Ridge Rd<br>
      Hollins, VA 24019
    </address>
  </section>

  <section class="card card-back" aria-label="Business card back">
    <div class="brand-mark" aria-hidden="true"></div>
    <p class="brand-name">Copper Vale</p>
    <div class="brand-suffix"><span class="rule"></span><span>LLC</span><span class="rule"></span></div>
  </section>
</main>
</body>
</html>
```